PTA Business Card

Seeking design for a business card, standard size. It is going to be for myself in regards to PTA - details:

Hollis Fernway Elementary School
PTA President
Neil Brawley
555-208-3147
Brawl1984@mailnest.example

Requirement:
Facebook icon? "Hollis Fernway PTA Durn"
Twitter thing? I am new to twitter so not sure what to put, here is the link:
https://twitter.com/HFRoverbirdsPTA

I was thinking on the front would be a notebook paper background? Not a requirement but was thinking it would look cool?

Total freedom here, let your creativity spread because I don't have any suggestions for design, sorry. Colors of school district are black and yellow.

Backside I am not sure exactly what to put on it.

```html
<!DOCTYPE html>
<html lang="en">
<head>
<meta charset="utf-8">
<title>Hollis Fernway Elementary School PTA – Business Card</title>
<link href="https://fonts.googleapis.com/css2?family=Cinzel:wght@400;500&family=Open+Sans:wght@300;400;700&display=swap" rel="stylesheet">
<style>
  :root {
    --page: #e9e7e2;
    --school-yellow: #f2ee3a;
    --school-black: #111111;
    --card-white: #ffffff;
    --ink: #2a2a2a;
    --ink-soft: #555555;
    --portrait-light: #d8d8d8;
    --portrait-dark: #6a6a6a;
    --social-square: #4a7bbf;
  }
  * { box-sizing: border-box; margin: 0; padding: 0; }
  html, body {
    width: 1200px; height: 1023px; overflow: hidden;
    background: var(--page);
  }
  .sheet {
    position: relative; width: 1200px; height: 1023px;
    display: flex; flex-direction: column; align-items: center; justify-content: center; gap: 40px;
  }
  .card {
    position: relative; width: 770px; height: 440px; overflow: hidden;
    box-shadow: 0 6px 18px rgba(0,0,0,.18);
  }

  /* front */
  .card-front { background: var(--card-white); }
  .title-band {
    position: absolute; left: 0; top: 0; width: 100%; height: 132px;
    background: var(--school-yellow);
    display: flex; flex-direction: column; align-items: center; justify-content: center;
  }
  .school-name {
    font-family: "Cinzel", serif; font-weight: 500;
    font-size: 52px; line-height: 1; color: var(--school-black); letter-spacing: 1px;
  }
  .school-type {
    display: flex; align-items: center; gap: 14px; margin-top: 8px;
    font-family: "Open Sans", sans-serif; font-size: 19px; letter-spacing: 2px;
    text-transform: uppercase; color: var(--school-black);
  }
  .school-type::before, .school-type::after {
    content: ""; width: 70px; height: 2px; background: currentColor;
  }
  .portrait {
    position: absolute; left: 0; top: 150px; width: 300px; height: 250px;
    background: linear-gradient(135deg, var(--portrait-dark), var(--portrait-light) 70%, var(--card-white));
  }
  .contact {
    position: absolute; left: 300px; right: 40px; top: 160px;
    text-align: center; font-family: "Open Sans", sans-serif; color: var(--ink);
  }
  .contact-name { font-size: 24px; font-weight: 400; text-transform: uppercase; letter-spacing: 1.5px; }
  .contact-role { font-size: 12px; text-transform: uppercase; letter-spacing: 1px; color: var(--ink-soft); margin-top: 2px; }
  .contact-phone { font-size: 15px; margin-top: 24px; }
  .contact-email { font-size: 15px; margin-top: 14px; }
  .social-row {
    position: absolute; left: 315px; right: 30px; top: 352px;
    display: flex; justify-content: space-between;
    font-family: "Open Sans", sans-serif; font-size: 14px; color: var(--ink);
  }
  .social-link { display: flex; align-items: center; gap: 8px; }
  .social-square { width: 16px; height: 16px; background: var(--social-square); border-radius: 2px; }
  .address-strip {
    position: absolute; left: 0; bottom: 0; width: 100%; height: 40px;
    background: var(--school-black);
    display: flex; align-items: center; justify-content: flex-end; padding-right: 28px;
    font-family: "Open Sans", sans-serif; font-weight: 700; font-size: 15px;
    text-transform: uppercase; color: var(--school-yellow); letter-spacing: .5px;
  }

  /* back */
  .card-back {
    background: linear-gradient(160deg, #2b2b2b, var(--school-black) 55%, #050505);
    display: flex; align-items: center; justify-content: center;
  }
  .back-portrait {
    position: absolute; left: 0; top: 0; width: 420px; height: 300px;
    background: radial-gradient(ellipse at 40% 45%, rgba(90,90,90,.35), rgba(0,0,0,0) 70%);
  }
  .card-back .school-name { color: var(--school-yellow); font-size: 48px; }
  .card-back .school-type { color: var(--school-yellow); }
  .back-title { position: relative; display: flex; flex-direction: column; align-items: center; margin-top: 60px; }
</style>
</head>
<body>
<main class="sheet">
  <section class="card card-front">
    <header class="title-band">
      <h1 class="school-name">Hollis Fernway</h1>
      <p class="school-type">Elementary School</p>
    </header>
    <div class="portrait" role="img" aria-label="Engraved-style portrait of the school's namesake"></div>
    <div class="contact">
      <p class="contact-name">Neil Brawley</p>
      <p class="contact-role">PTA President</p>
      <p class="contact-phone">555-208-3147</p>
      <p class="contact-email">Brawl1984@mailnest.example</p>
    </div>
    <div class="social-row">
      <span class="social-link"><span class="social-square"></span>Hollis Fernway PTA Durn</span>
      <span class="social-link"><span class="social-square"></span>/HFRoverbirdsPTA</span>
    </div>
    <footer class="address-strip">2240 Larkmoor Lane, Elderby, Any State</footer>
  </section>

  <section class="card card-back">
    <div class="back-portrait" role="img" aria-label="Faint dark portrait of the school's namesake"></div>
    <div class="back-title">
      <h2 class="school-name">Hollis Fernway</h2>
      <p class="school-type">Elementary School</p>
    </div>
  </section>
</main>
</body>
</html>
```